Pastured Free Range Egg farm needs carton label

We have recently updated our logo, and are looking to incorporate the new logo into a new design for our dozen size egg cartons. (New logo has been included in the uploads - there are several file formats available, so let me know if you need a different file format for the logo.)
We are a company that is focused on ethical farming, and the welfare of our hens. We are a small, niche farm, run by a husband and wife and 3 children.
I have included a photo of our farm and the trailers we use for our hens so that you can see the type of farming methods we use.
We would like to keep the label relaxed, to reflect the small family business.
We would like the use of green colours to represent the "pastured" aspect of our egg farming. We want the label to represent our better farming practices.
We have included a graphic of our current label which we like the feel and style of.
We have also included a graphic of the dieline that must be used so we can submit the design to the printing company. (we do not need a space for a barcode on our label)
______________
Things that must be included legally on the label:
* The words "12 Pastured Free Range Eggs",
*Nutrition label panel as pictured in the current label graphic
* Weight options as pictured in the current label the words "Min Total Mass" must be used and have a selection for weights of 600gm, 700gm and 800gm
* Chicken stocking density must be prominent to show our care for the hens the words "150 chickens per hectare" must be used
* A best before section where we can stamp a date
* A product of Australia logo
* The words "Commercial reuse of this carton prohibited" on the back of the carton
* A "please recycle" logo on the back of the carton
* Farm details on the back of the carton:
Marlow Farm
T & K Marlow
18 Pemberly Rd
Elmsworth VIC 3712
Ph: 0491 578 306
I would like some information on our farming practices like what is pictured on the original label:
" Our hens are housed in mobile trailers that are moved to fresh pasture regularly on our farm in Elmsworth, Victoria.
The hens have access to the outdoors 24 hours a day. They have plenty of room to flap their wings, and to scratch and forage for bugs.
Our hens are happy and healthy, help to sustain our land, and lay us these delicious eggs!"
Target Market(s)
People wanting ethical sustainable produce
Look and feel

```html
<!DOCTYPE html>
<html lang="en">
<head>
<meta charset="utf-8">
<title>Marlow Farm – Egg Carton Label</title>
<link rel="stylesheet" href="https://fonts.googleapis.com/css2?family=Open+Sans:wght@400;600;700;800&family=Oswald:wght@300;400&display=swap">
<style>
:root{
  --bg:#8f8f8f;
  --paper:#ffffff;
  --forest:#004f2d;
  --olive:#7d7f05;
  --olive-line:#848200;
  --table-green:#8ccf6e;
  --table-light:#d5eec8;
  --hen-light:#d98a3c;
  --hen-dark:#8e3f12;
}
*{margin:0;padding:0;box-sizing:border-box}
html,body{width:1200px;height:877px;overflow:hidden;background:var(--bg)}
.canvas{position:relative;width:1200px;height:877px;font-family:"Open Sans",Arial,sans-serif}
.dieline{position:absolute;left:0;top:0}

/* back panel (printed upside-down) */
.back-panel{position:absolute;left:109px;top:140px;width:983px;height:136px;transform:rotate(180deg);color:var(--forest)}
.practices{position:absolute;left:31px;top:38px;width:336px;font-size:7.4px;line-height:10.6px;text-transform:uppercase;text-align:justify;text-align-last:justify;font-weight:600}
.practices span{display:block}
.practices .last{text-align-last:left}
.divider{position:absolute;width:1.5px;background:var(--forest)}
.divider.one{left:377px;top:31px;height:76px}
.divider.two{left:500px;top:31px;height:76px}
.farm-details{position:absolute;left:389px;top:38px;font-size:7.6px;line-height:13px;text-transform:uppercase;font-weight:600;font-style:normal}
.made-badge{position:absolute;left:513px;top:24px}
.recycle-badge{position:absolute;left:517px;top:74px}
.reuse-note{position:absolute;left:510px;top:114px;font-size:6.4px;font-weight:700;color:var(--forest);letter-spacing:.1px;white-space:nowrap}
.serving{position:absolute;left:610px;top:27px;font-size:6.2px;line-height:8.6px;color:#222}
.serving .head{font-weight:800;margin-bottom:2px}
.serving .sizes{background:var(--table-green);padding:1px 3px;width:104px;font-weight:600}
.serving .note{margin-top:2px}
.nutrition{position:absolute;left:737px;top:25px;width:218px;height:98px;border:2px solid var(--table-green);padding:2px 3px;font-size:5.2px;color:#222}
.nutrition h4{font-size:7.2px;font-weight:800;line-height:8px}
.nutrition .meta{font-weight:700;line-height:7px;border-bottom:1.5px solid var(--table-green);margin-bottom:1px}
.nutrition table{width:100%;border-collapse:collapse}
.nutrition th,.nutrition td{padding:0 2px;line-height:6.4px;text-align:left;border-left:1px solid var(--table-green)}
.nutrition th:first-child,.nutrition td:first-child{border-left:0}
.nutrition th{font-weight:700;background:var(--table-green)}
.nutrition tr:nth-child(even) td{background:var(--table-light)}

/* front */
.brand{position:absolute;display:flex;align-items:center;gap:8px;font-weight:700;white-space:nowrap}
.brand .dot{border-radius:50%;display:block}
.brand.front{left:160px;top:400px;font-size:29px;color:var(--forest)}
.brand.front .dot{width:18px;height:18px;background:var(--forest)}
.brand.bottom{left:552px;top:668px;font-size:19px;color:var(--paper)}
.brand.bottom .dot{width:12px;height:12px;background:var(--paper)}

.egg-title{position:absolute;left:436px;top:318px;width:320px;text-align:center;color:var(--olive);font-weight:800}
.egg-title span,.mini-title span{display:block}
.egg-title .count{font-size:56px;line-height:56px}
.egg-title .line{font-size:40px;line-height:41px;letter-spacing:-.3px}
.mini-title{position:absolute;left:262px;top:619px;width:180px;text-align:center;color:var(--paper);font-weight:800}
.mini-title .count{font-size:28px;line-height:28px}
.mini-title .line{font-size:19px;line-height:20px}

.density{position:absolute;left:912px;top:470px;width:200px;text-align:center;color:var(--paper);font-family:"Oswald",Arial,sans-serif;font-weight:400;font-size:31px;line-height:36px;letter-spacing:1.5px;transform:rotate(-16deg)}

.mass{position:absolute;left:799px;top:621px;color:var(--paper);font-family:"Oswald",Arial,sans-serif;font-weight:300;font-size:18px;line-height:21px;letter-spacing:.8px}
.mass li{list-style:none;display:flex;align-items:center;gap:5px}
.mass .box{width:14px;height:14px;border-radius:4px;background:var(--paper)}
.mass .label{margin-top:2px}
</style>
</head>
<body>
<div class="canvas">
  <svg class="dieline" width="1200" height="877" viewBox="0 0 1200 877">
    <defs>
      <clipPath id="front-band">
        <rect x="64" y="276" width="1072" height="326" rx="47"/>
      </clipPath>
      <radialGradient id="hen-tone" cx="45%" cy="40%" r="70%">
        <stop offset="0" stop-color="#d98a3c"/>
        <stop offset="1" stop-color="#8e3f12"/>
      </radialGradient>
    </defs>
    <rect class="panel-back" x="109" y="140" width="983" height="180" rx="27" fill="var(--paper)"/>
    <rect class="panel-base" x="109" y="560" width="983" height="177" rx="27" fill="var(--forest)"/>
    <rect class="panel-front" x="64" y="276" width="1072" height="326" rx="47" fill="var(--paper)"/>
    <g role="img" aria-label="Photo of a brown hen looking left">
      <path d="M862 486 C856 420 858 330 900 300 C950 285 1000 310 1030 360 C1040 400 1035 450 1030 486 Z" fill="url(#hen-tone)"/>
    </g>
    <g clip-path="url(#front-band)">
      <path d="M64 443 Q598 652 1136 396 L1136 610 L64 610 Z" fill="var(--forest)"/>
      <path d="M64 439 Q598 648 1136 392" fill="none" stroke="var(--olive-line)" stroke-width="6"/>
    </g>
    <path class="egg-outline" d="M530 382 C545 330 570 299 596 299 C622 299 650 330 664 382" fill="none" stroke="var(--olive-line)" stroke-width="5"/>
    <path class="egg-outline" d="M536 470 C546 499 570 513 596 513 C624 513 648 499 657 470" fill="none" stroke="var(--olive-line)" stroke-width="5"/>
    <path class="egg-outline-mini" d="M321 650 C328 624 338 609 352 609 C366 609 377 624 384 650" fill="none" stroke="var(--paper)" stroke-width="3"/>
    <path class="egg-outline-mini" d="M323 694 C330 707 340 713 352 713 C364 713 374 707 381 694" fill="none" stroke="var(--paper)" stroke-width="3"/>
    <rect class="tab-slot" x="163" y="598" width="86" height="86" rx="14" fill="var(--bg)"/>
    <rect class="tab-slot" x="944" y="598" width="86" height="86" rx="14" fill="var(--bg)"/>
  </svg>

  <section class="back-panel">
    <p class="practices">
      <span>Our hens are housed in mobile trailers that are moved to fresh</span>
      <span>pasture regularly on our farm in Elmsworth, Victoria.</span>
      <span>The hens have access to the outdoors 24 hours a day. They have</span>
      <span>plenty of room to flap their wings, and to scratch and forage</span>
      <span>for bugs. Our hens are happy and healthy, help to sustain our land,</span>
      <span class="last">and lay us these delicious eggs!</span>
    </p>
    <div class="divider one"></div>
    <address class="farm-details">
      Marlow Farm<br>T &amp; K Marlow<br>18 Pemberly Rd<br>Elmsworth VIC 3712<br>Ph: 0491 578 306
    </address>
    <div class="divider two"></div>
    <svg class="made-badge" width="43" height="42" viewBox="0 0 43 42" role="img" aria-label="Product of Australia badge">
      <path d="M0 0 H43 L21.5 42 Z" fill="#0f7a55"/>
    </svg>
    <svg class="recycle-badge" width="34" height="34" viewBox="0 0 34 34" role="img" aria-label="Please recycle badge">
      <circle cx="17" cy="17" r="16" fill="#2ea564"/>
    </svg>
    <p class="reuse-note">COMMERCIAL REUSE OF THIS CARTON PROHIBITED</p>
    <div class="serving">
      <p class="head">PACK SERVING SIZES:</p>
      <p class="sizes">600g pack = 90g (2 eggs)*<br>700g pack = 104g (2 eggs)*<br>800g pack = 118g (2 eggs)*</p>
      <p class="note">*Edible portion only.<br>Average quantities listed.</p>
    </div>
    <div class="nutrition">
      <h4>NUTRITION INFORMATION</h4>
      <p class="meta">SERVINGS PER PACK: 6 SERVING SIZE: 2 Eggs* (see list on left for serving size)</p>
      <table>
        <tr><th></th><th>AVG. QTY. PER 90g SERVE</th><th>AVG. QTY. PER 104g SERVE</th><th>AVG. QTY. PER 118g SERVE</th><th>AVG. QTY. PER 100g</th></tr>
        <tr><td>Energy</td><td>530kJ</td><td>620kJ</td><td>703kJ</td><td>598kJ</td></tr>
        <tr><td>Protein</td><td>11.0g</td><td>12.7g</td><td>14.4g</td><td>12.2g</td></tr>
        <tr><td>Fat, total</td><td>8.5g</td><td>10.0g</td><td>11.3g</td><td>9.6g</td></tr>
        <tr><td>– saturated</td><td>3.0g</td><td>3.4g</td><td>3.8g</td><td>3.3g</td></tr>
        <tr><td>Carbohydrate</td><td>1.2g</td><td>1.4g</td><td>1.5g</td><td>1.3g</td></tr>
        <tr><td>– sugars</td><td>0.3g</td><td>0.3g</td><td>0.4g</td><td>0.3g</td></tr>
        <tr><td>Sodium</td><td>122mg</td><td>141mg</td><td>160mg</td><td>136mg</td></tr>
      </table>
    </div>
  </section>

  <div class="brand front"><span class="dot"></span>Marlow Farm</div>

  <h1 class="egg-title">
    <span class="count">12</span>
    <span class="line">PASTURED FREE</span>
    <span class="line">RANGE EGGS</span>
  </h1>

  <p class="density">150 CHICKENS<br>PER HECTARE</p>

  <div class="mini-title">
    <span class="count">12</span>
    <span class="line">PASTURED FREE</span>
    <span class="line">RANGE EGGS</span>
  </div>

  <div class="brand bottom"><span class="dot"></span>Marlow Farm</div>

  <ul class="mass">
    <li><span class="box"></span>600GM</li>
    <li><span class="box"></span>700GM</li>
    <li><span class="box"></span>800GM</li>
    <li class="label">MIN TOTAL MASS</li>
  </ul>
</div>
</body>
</html>
```